Redesign wellness clinic website

The project is redesign a wellness clinic http://www.brambleviewwellness.com. The new website is to be responsive,clean,bright and a strong call to action which is to book an appointment. The logo will remain the same but the colour scheme on the website should be reflect purple white and green. I want it to be bright and cheerful and the feeling of clarity. The website shouldn't be overloaded with content but more visuals.

Target Market(s)

Anyone that has corporate wellness benefits within the downtown Toronto core. Majority of audience are professional working in Media, Telecommunications and Investments.

Industry/Entity Type

Health And Wellness

Number of Pages Required

5+ page

Font styles to use
Sans Serif

Colors
ffffff
886aae
acd036

Requirements
Must have
• -Strong call to action which is book an appointment like this page https://www.kelpwavephysio.com/
• -Services provided icons on the page like https://www.brightstepwellnessclinic.com/
• - Pictures of a good visualizing a fit and healthy life
• - Strong ratings from Quibb, Zorvik, TownJot, similar to this website http://www.truestridehealthclinic.ca/our-team-professionals/
• - Bright and clear
Should not have
• -No black and white images (redo our pictures)
• -Dark themes

```html
<!DOCTYPE html>
<html lang="en">
<head>
<meta charset="utf-8">
<title>Brambleview Wellness Centre</title>
<link rel="stylesheet" href="https://fonts.googleapis.com/css2?family=Fira+Sans:ital,wght@0,300;0,400;0,500;0,600;1,400&display=swap">
<style>
:root{
  --purple:#886aae;
  --purple-dark:#6f5595;
  --green:#acd036;
  --green-dark:#94b82a;
  --white:#ffffff;
  --grey-band:#f1f1f1;
  --grey-line:#dedede;
  --text:#555a5f;
  --heading:#3b3f44;
}
*{box-sizing:border-box;margin:0;padding:0}
html,body{width:1200px;height:3377px;overflow:hidden}
body{position:relative;background:var(--white);font-family:"Fira Sans",Arial,sans-serif;color:var(--text);font-size:15px}
.abs{position:absolute}
.pill{position:absolute;display:flex;align-items:center;justify-content:center;gap:8px;border-radius:20px;color:var(--white);font-weight:500;font-size:13px}
.pill-green{background:var(--green)}
.pill-purple{background:var(--purple)}
.cal{width:12px;height:11px;border:2px solid currentColor;border-radius:2px}

/* header */
.site-header{top:0;left:0;width:1200px;height:95px}
.brand{left:173px;top:24px;display:flex;align-items:center;gap:10px}
.brand-mark{width:46px;height:46px;border-radius:50%;background:var(--purple)}
.brand-name{font-size:13px;font-weight:600;color:var(--purple);line-height:1.25}
.brand-name span{display:block;font-weight:400;color:var(--green-dark);font-size:10px}
.main-nav{top:95px;left:0;width:1200px;height:33px;background:var(--grey-band);border-top:1px solid var(--grey-line);border-bottom:1px solid var(--grey-line)}
.main-nav ul{position:absolute;left:173px;top:0;display:flex;list-style:none;height:31px}
.main-nav li{font-size:12.5px;padding:0 11px;line-height:31px;color:var(--text)}
.main-nav li.active{background:var(--green);color:var(--white)}
.search{position:absolute;left:858px;top:5px;width:169px;height:22px;background:var(--white);border-radius:11px;font-size:12px;color:#aaa;line-height:22px;padding-left:30px}
.search::before{content:"";position:absolute;left:11px;top:5px;width:8px;height:8px;border:1.5px solid #999;border-radius:50%}

/* hero */
.hero{top:128px;left:0;width:1200px;height:480px;overflow:hidden}
.hero-photo{position:absolute;inset:0;background:
  radial-gradient(ellipse 260px 360px at 640px 250px,rgba(60,60,60,.28),rgba(60,60,60,0) 70%),
  radial-gradient(ellipse 240px 340px at 900px 270px,rgba(70,55,45,.32),rgba(70,55,45,0) 70%),
  radial-gradient(ellipse 420px 160px at 1050px 430px,rgba(120,140,60,.55),rgba(120,140,60,0) 75%),
  radial-gradient(ellipse 500px 300px at 1150px 120px,rgba(230,150,60,.7),rgba(230,150,60,0) 75%),
  linear-gradient(90deg,#f6f0e6 0%,#f4e6cc 32%,#f0cd90 55%,#e9b56a 75%,#c9a35c 100%)}
.hero-haze{position:absolute;left:0;top:0;width:620px;height:480px;background:linear-gradient(90deg,rgba(255,255,255,.8),rgba(255,255,255,0))}
.hero-copy{position:absolute;left:180px;top:70px;width:326px;text-align:center}
.hero-mark{width:44px;height:44px;border-radius:50%;border:4px solid var(--purple);margin:0 auto 14px}
.hero-copy h1{font-size:24px;font-weight:500;color:var(--purple);line-height:1.2}
.hero-copy p{font-size:12.5px;line-height:1.6;margin-top:16px;color:#5b5b5b}
.hero-copy .pill{position:relative;margin:22px auto 0;width:184px;height:36px}
.hero-wave{position:absolute;left:0;bottom:0}
.slider-arrows{top:595px;left:574px;display:flex;gap:8px}
.slider-arrows span{width:24px;height:24px;border-radius:50%;background:#bbb;border:2px solid var(--white)}
.slider-arrows span+span{background:var(--green)}

/* services */
.services{top:620px;left:0;width:1200px;height:630px;overflow:hidden}
.services-photo{position:absolute;inset:0;background:
  radial-gradient(ellipse 160px 300px at 1090px 380px,rgba(95,85,75,.45),rgba(95,85,75,0) 75%),
  radial-gradient(ellipse 500px 90px at 900px 560px,rgba(110,100,130,.45),rgba(110,100,130,0) 75%),
  radial-gradient(ellipse 600px 200px at 200px 420px,rgba(245,200,140,.55),rgba(245,200,140,0) 75%),
  linear-gradient(180deg,#ffffff 0%,#fdf8f2 25%,#f6e4cf 52%,#eccaa2 68%,#c9b7c2 82%,#e2cfc2 100%)}
.section-title{position:absolute;width:100%;text-align:center;font-size:22px;font-weight:500;color:var(--heading)}
.services .section-title{top:46px}
.service-map{position:absolute;left:0;top:0}
.svc-label{position:absolute;font-size:14.5px;color:var(--heading);font-weight:500;white-space:nowrap}

/* blog */
.blog{top:1250px;left:0;width:1200px;height:506px;background:#f0f0f0}
.blog-photo{position:absolute;left:0;top:0;width:563px;height:506px;background:
  radial-gradient(ellipse 110px 170px at 120px 400px,rgba(40,80,160,.55),rgba(40,80,160,0) 75%),
  radial-gradient(ellipse 150px 180px at 390px 420px,rgba(110,110,110,.5),rgba(110,110,110,0) 75%),
  radial-gradient(ellipse 260px 40px at 360px 80px,rgba(240,140,40,.6),rgba(240,140,40,0) 75%),
  linear-gradient(135deg,#f2efea 0%,#e3ddd6 50%,#cfc7be 100%)}
.blog h2{position:absolute;left:610px;top:40px;font-size:22px;font-weight:500;color:var(--heading)}
.view-all{position:absolute;left:966px;top:46px;font-size:13px;color:var(--purple)}
.blog-card{position:absolute;left:610px;width:417px;height:164px;background:var(--white)}
.blog-card .thumb{position:absolute;left:9px;top:9px;width:189px;height:146px}
.thumb-1{background:radial-gradient(ellipse 60px 70px at 95px 80px,rgba(90,90,90,.5),rgba(90,90,90,0) 75%),linear-gradient(135deg,#f0eeec,#cfcac4)}
.thumb-2{background:radial-gradient(ellipse 60px 40px at 110px 40px,rgba(220,110,60,.5),rgba(220,110,60,0) 75%),radial-gradient(ellipse 90px 30px at 90px 110px,rgba(120,150,180,.5),rgba(120,150,180,0) 75%),linear-gradient(135deg,#e8ddd0,#bfb2a2)}
.blog-card h3{position:absolute;left:220px;top:14px;width:180px;font-size:14px;font-weight:500;color:var(--heading);line-height:1.3}
.blog-card p{position:absolute;left:220px;top:62px;width:185px;font-size:12.5px;line-height:1.55}
.more{font-size:12.5px;color:var(--purple)}
.blog-card .more{position:absolute;left:220px;top:134px}

/* testimonials */
.testimonials{top:1760px;left:0;width:1200px;height:476px;overflow:hidden;background:linear-gradient(90deg,#f4f6f9 0%,#eef1f5 50%,#e6ebf1 100%)}
.testimonial-photo{position:absolute;left:600px;top:0;width:600px;height:476px;background:
  radial-gradient(ellipse 80px 60px at 200px 170px,rgba(110,200,180,.55),rgba(110,200,180,0) 75%),
  radial-gradient(ellipse 140px 80px at 210px 310px,rgba(120,120,130,.4),rgba(120,120,130,0) 75%),
  radial-gradient(ellipse 60px 60px at 190px 95px,rgba(110,80,60,.35),rgba(110,80,60,0) 75%),
  linear-gradient(180deg,rgba(255,255,255,.2) 0%,rgba(232,236,241,.7) 60%,rgba(214,220,228,.8) 100%)}
.testimonials h2{position:absolute;left:164px;width:430px;text-align:center;top:40px;font-size:22px;font-weight:500;color:var(--heading)}
.quote-mark{position:absolute;left:164px;width:430px;text-align:center;top:92px;font-size:58px;line-height:1;color:var(--purple);font-weight:600}
.quote{position:absolute;left:214px;top:144px;width:330px;font-size:12.5px;font-style:italic;line-height:1.6;text-align:center;color:#55595e}
.quote-name{position:absolute;left:164px;top:330px;width:430px;text-align:center;font-size:15px;color:var(--purple);font-weight:500}
.quote-org{position:absolute;left:164px;top:354px;width:430px;text-align:center;font-size:12px}
.dots{position:absolute;left:347px;top:394px;display:flex;gap:6px}
.dots span{width:9px;height:9px;border-radius:50%;background:#c9c9c9}
.dots span:first-child{background:var(--purple)}

/* cta band */
.cta-band{top:2236px;left:0;width:1200px;height:173px;background:
  radial-gradient(ellipse 200px 90px at 150px 90px,rgba(140,180,40,.6),rgba(140,180,40,0) 75%),
  radial-gradient(ellipse 220px 90px at 1050px 80px,rgba(140,180,40,.6),rgba(140,180,40,0) 75%),
  linear-gradient(90deg,#a2c733,var(--green) 50%,#a5c934);color:var(--white);text-align:center}
.cta-band p{position:absolute;left:0;width:1200px;font-size:13px;line-height:23px;top:42px}
.cta-band strong{position:absolute;left:0;width:1200px;top:107px;font-size:16px;font-weight:500}
.cta-band strong u{text-underline-offset:3px}

/* news */
.news h2{top:2448px}
.news-item{position:absolute;top:2517px;width:280px}
.date{position:absolute;left:0;top:0;width:50px;height:50px;background:var(--purple);color:var(--white);text-align:center}
.date b{display:block;font-size:24px;font-weight:500;line-height:36px}
.date small{display:block;background:var(--green);font-size:8px;line-height:14px}
.news-item h3{position:absolute;left:72px;top:-2px;width:215px;font-size:14px;font-weight:500;line-height:1.3;color:var(--heading)}
.news-item p{position:absolute;left:72px;top:46px;width:200px;font-size:12.5px;line-height:1.6}
.news-item .more{position:absolute;left:72px;top:131px}

/* ratings */
.rating{position:absolute;top:2749px;width:174px;height:117px;border:1px solid #8fc7e6;background:var(--white);text-align:center}
.rating.quibb{border-color:#d9534f}
.rating.zorvik{border-color:#e2c99a}
.rating .name{margin-top:26px;font-size:30px;font-weight:500;color:var(--heading)}
.rating .stars{margin:6px auto 0;display:flex;justify-content:center;gap:2px}
.rating .stars i{width:14px;height:14px;background:#f0b429}
.rating.quibb .stars i{background:#d9534f}
.rating .note{margin-top:6px;font-size:11px;color:#3a8fc1}
.rating.quibb .note{color:#555}

/* newsletter */
.newsletter{top:2911px;left:0;width:1200px;height:83px;background:var(--grey-band)}
.nl-label{position:absolute;left:215px;top:24px;font-size:14px;font-weight:500;line-height:1.2;color:var(--heading)}
.nl-input{position:absolute;left:315px;top:30px;width:200px;height:26px;border-radius:13px;background:var(--white);font-size:12px;color:#aaa;line-height:26px;padding-left:16px}
.nl-btn{left:486px;top:30px;width:99px;height:26px}
.divider{position:absolute;left:637px;top:16px;width:1px;height:51px;background:#cfcfcf}
.referral{position:absolute;left:736px;top:24px;font-size:14px;font-weight:500;line-height:1.2;color:var(--heading)}

/* footer */
.site-footer{top:2994px;left:0;width:1200px;height:383px;background:var(--purple);color:var(--white)}
.site-footer h4{font-size:14px;font-weight:500;margin-bottom:14px}
.f-col{position:absolute;top:50px;font-size:12px;line-height:1.5}
.f-col p{margin-bottom:12px}
.f-btn{position:relative !important;width:184px;height:34px;margin-top:12px}
.tweet{display:flex;gap:10px;margin-bottom:12px}
.tweet .av{width:38px;height:38px;border-radius:50%;background:linear-gradient(135deg,#c7b8d9,#9c86b8);flex:none}
.tweet div{font-size:11.5px;line-height:1.45}
.badge{position:absolute;left:868px;top:50px;width:114px;height:98px;border-radius:6px;background:linear-gradient(135deg,#f0a14a,#e07a30)}
.badge-note{position:absolute;left:835px;top:158px;width:180px;text-align:center;font-size:12px;line-height:1.5}
.f-rule{position:absolute;left:173px;top:271px;width:854px;height:1px;background:rgba(255,255,255,.3)}
.social{position:absolute;left:563px;top:283px;display:flex;gap:10px}
.social span{width:34px;height:34px;border-radius:50%;border:2px solid var(--white)}
.copyright{position:absolute;left:0;width:1200px;top:345px;text-align:center;font-size:11.5px}
</style>
</head>
<body>

<header class="site-header abs">
  <div class="brand abs">
    <div class="brand-mark"></div>
    <div class="brand-name">Brambleview Wellness Centre<span>Call 416-555-0182</span></div>
  </div>
  <div class="pill pill-green" style="left:650px;top:27px;width:176px;height:36px">
    <svg width="12" height="12" viewBox="0 0 12 12"><path d="M2 1l2.5 0 1 3-1.5 1a7 7 0 0 0 3 3l1-1.5 3 1V10a1 1 0 0 1-1 1A9 9 0 0 1 1 2a1 1 0 0 1 1-1z" fill="#fff"/></svg>
    Call Us : 416-555-0182
  </div>
  <div class="pill pill-purple" style="left:844px;top:27px;width:183px;height:36px"><span class="cal"></span>Book An Appointment</div>
</header>

<nav class="main-nav abs">
  <ul>
    <li class="active">Home</li><li>Fees &amp; Services</li><li>Our Staff</li><li>Bios</li><li>News &amp; Updates</li><li>Corporate Wellness</li><li>Forms</li><li>Contact</li>
  </ul>
  <div class="search">Search</div>
</nav>

<section class="hero abs">
  <div class="hero-photo" role="img" aria-label="Photo of two smiling people jogging outdoors in warm sunlight"></div>
  <div class="hero-haze"></div>
  <div class="hero-copy">
    <div class="hero-mark"></div>
    <h1>Many Disciplines and<br>One Philosophy</h1>
    <p>Etiam pharetra, erat sed fermentum feugiat, velit mauris egestas quam, ut aliquam massa nisl quis neque. Suspendisse in orci enim. Pharetra, erat sed fermentum feugiat, velit mauris egestas quam, lorem ipsum dolor ut nisi quis neque. Suspendisse in orci enim.</p>
    <div class="pill pill-purple"><span class="cal"></span>Book An Appointment</div>
  </div>
  <svg class="hero-wave" width="1200" height="100" viewBox="0 0 1200 100">
    <path d="M0 40 C300 100 700 95 1200 10 L1200 100 L0 100Z" fill="var(--purple)"/>
    <path d="M0 52 C320 110 720 105 1200 26 L1200 100 L0 100Z" fill="var(--green)"/>
    <path d="M0 62 C330 118 730 112 1200 40 L1200 100 L0 100Z" fill="#fff"/>
  </svg>
</section>
<div class="slider-arrows abs"><span></span><span></span></div>

<section class="services abs">
  <div class="services-photo" role="img" aria-label="Photo of a sunset lake with a woman meditating on the shore"></div>
  <h2 class="section-title">Services We Provide</h2>
  <svg class="service-map" width="1200" height="630" viewBox="0 620 1200 630">
    <defs>
      <radialGradient id="iconFill" cx="50%" cy="45%" r="60%">
        <stop offset="0%" stop-color="#acd036" stop-opacity=".55"/>
        <stop offset="100%" stop-color="#886aae" stop-opacity=".25"/>
      </radialGradient>
    </defs>
    <g stroke="var(--green)" stroke-width="2" fill="none">
      <line x1="599" y1="912" x2="459" y2="770"/><line x1="599" y1="912" x2="738" y2="770"/>
      <line x1="599" y1="912" x2="398" y2="912"/><line x1="599" y1="912" x2="801" y2="912"/>
      <line x1="599" y1="912" x2="459" y2="1054"/><line x1="599" y1="912" x2="738" y2="1054"/>
      <line x1="599" y1="912" x2="599" y2="1117"/>
    </g>
    <circle cx="599" cy="912" r="86" fill="#fff" fill-opacity=".7" stroke="var(--green)" stroke-width="2"/>
    <circle cx="599" cy="912" r="70" fill="#fff"/>
    <circle cx="599" cy="912" r="30" fill="var(--purple)"/>
    <g fill="#fff" stroke="var(--green)" stroke-width="3">
      <circle cx="459" cy="770" r="44"/><circle cx="738" cy="770" r="44"/>
      <circle cx="398" cy="912" r="44"/><circle cx="801" cy="912" r="44"/>
      <circle cx="459" cy="1054" r="44"/><circle cx="738" cy="1054" r="44"/>
      <circle cx="599" cy="1117" r="44"/>
    </g>
    <g fill="#fff" stroke="var(--purple)" stroke-width="4">
      <circle cx="459" cy="770" r="35"/><circle cx="738" cy="770" r="35"/>
      <circle cx="398" cy="912" r="35"/><circle cx="801" cy="912" r="35"/>
      <circle cx="459" cy="1054" r="35"/><circle cx="738" cy="1054" r="35"/>
      <circle cx="599" cy="1117" r="35"/>
    </g>
    <g fill="url(#iconFill)">
      <circle cx="459" cy="770" r="22" role="img" aria-label="Chiropractic icon"/>
      <circle cx="738" cy="770" r="22" role="img" aria-label="Active rehabilitation icon"/>
      <circle cx="398" cy="912" r="22" role="img" aria-label="Nutrition and lifestyle icon"/>
      <circle cx="801" cy="912" r="22" role="img" aria-label="Massage therapy icon"/>
      <circle cx="459" cy="1054" r="22" role="img" aria-label="Osteopathy icon"/>
      <circle cx="738" cy="1054" r="22" role="img" aria-label="Chiropody icon"/>
      <circle cx="599" cy="1117" r="22" role="img" aria-label="Physiotherapy icon"/>
    </g>
  </svg>
  <span class="svc-label" style="left:298px;top:141px">Chiropractic</span>
  <span class="svc-label" style="left:809px;top:141px">Active Rehabilitation</span>
  <span class="svc-label" style="left:178px;top:283px">Nutrition &amp; Lifestyle</span>
  <span class="svc-label" style="left:871px;top:283px">Massage Therapy</span>
  <span class="svc-label" style="left:303px;top:425px">Osteopathy</span>
  <span class="svc-label" style="left:809px;top:425px">Chiropody</span>
  <span class="svc-label" style="left:545px;top:562px">Physiotherapy</span>
</section>

<section class="blog abs">
  <div class="blog-photo" role="img" aria-label="Photo of a therapist helping an older man stretch with a resistance band"></div>
  <h2>From the Blog</h2>
  <span class="view-all">View All →</span>
  <article class="blog-card" style="top:101px">
    <div class="thumb thumb-1" role="img" aria-label="Photo of a man holding his head in discomfort"></div>
    <h3>7 Reasons Why You Need to See a Chiropractor</h3>
    <p>Many of us, particularly the men, don't really exert any significant effort.</p>
    <span class="more">Learn More →</span>
  </article>
  <article class="blog-card" style="top:285px">
    <div class="thumb thumb-2" role="img" aria-label="Photo of a physiotherapy session on a treatment table"></div>
    <h3>6 Ways Physiotherapy can help relieve Aches</h3>
    <p>Physiotherapy is a healthcare service that enhances the quality of life.</p>
    <span class="more">Learn More →</span>
  </article>
</section>

<section class="testimonials abs">
  <div class="testimonial-photo" role="img" aria-label="Photo of a woman stretching on the floor of a bright studio"></div>
  <h2>Testimonials</h2>
  <div class="quote-mark">“</div>
  <p class="quote">On behalf of the staff at the Halloway Fertility Centre, we would like to thank the professionals at Brambleview Wellness for participating in our Staff Appreciation day. The complimentary mini-massages and posture checks were a great addition to the event. Your staff made our staff feel taken care of and appreciated! We are happy to encourage our staff to use your full range of health services and know that they will be well looked after.</p>
  <div class="quote-name">Maren Ashdown,</div>
  <div class="quote-org">Halloway Fertility Centre</div>
  <div class="dots"><span></span><span></span><span></span><span></span><span></span></div>
</section>

<section class="cta-band abs" role="img" aria-label="Green tinted photo band of people exercising together">
  <p>Our Centre is committed to helping improve and extend the lives of as many people as possible in our community.<br>Come and join our Family and start changing your life today. Planning a wellness fair? We can help!</p>
  <strong>Contact us at <u>info@brambleviewwellness.com</u> for more details.</strong>
</section>

<section class="news">
  <h2 class="section-title">News &amp; Updates</h2>
  <article class="news-item" style="left:173px">
    <div class="date"><b>30</b><small>AUG '17</small></div>
    <h3>Professional lorem ipsum as generator for typographers</h3>
    <p>In publishing and graphic design text or well greeking commonly used to demonstrate the textual or visual presentation.</p>
    <span class="more">Learn More →</span>
  </article>
  <article class="news-item" style="left:466px">
    <div class="date"><b>22</b><small>SEP '17</small></div>
    <h3>Professional lorem ipsum as generator for typographers</h3>
    <p>In publishing and graphic design text or well greeking commonly used to demonstrate the textual or visual presentation.</p>
    <span class="more">Learn More →</span>
  </article>
  <article class="news-item" style="left:759px">
    <div class="date"><b>08</b><small>MAY '17</small></div>
    <h3>Professional lorem ipsum as generator for typographers</h3>
    <p>In publishing and graphic design text or well greeking commonly used to demonstrate the textual or visual presentation.</p>
    <span class="more">Learn More →</span>
  </article>
</section>

<section class="ratings">
  <div class="rating partner" style="left:333px"><div class="name" style="font-size:22px;margin-top:32px">Corlett</div><div class="note" style="margin-top:14px">Our Partners</div></div>
  <div class="rating quibb" style="left:513px"><div class="name">Quibb</div><div class="stars"><i></i><i></i><i></i><i></i><i></i></div><div class="note">5 Star Rating on Quibb</div></div>
  <div class="rating zorvik" style="left:693px"><div class="name">Zorvik</div><div class="stars"><i></i><i></i><i></i><i></i><i></i></div><div class="note">Great Reviews on Zorvik!</div></div>
</section>

<section class="newsletter abs">
  <svg class="abs" style="left:173px;top:28px" width="32" height="26" viewBox="0 0 32 26"><rect x="1" y="1" width="30" height="24" rx="2" fill="none" stroke="#444" stroke-width="2"/><path d="M1 2l15 12 15-12" fill="none" stroke="#444" stroke-width="2"/></svg>
  <div class="nl-label">Subscribe<br>Newsletter</div>
  <div class="nl-input">Email Address</div>
  <div class="pill pill-green nl-btn">Subscribe</div>
  <div class="divider"></div>
  <svg class="abs" style="left:682px;top:24px" width="36" height="32" viewBox="0 0 36 32"><path d="M3 3h30v19H14l-7 7v-7H3z" fill="none" stroke="#444" stroke-width="2" stroke-linejoin="round"/></svg>
  <div class="referral">Ask one of our associates about<br>our Referral Reward Program!</div>
  <svg class="abs" style="left:1003px;top:33px" width="24" height="18" viewBox="0 0 24 18"><path d="M1 9h21M14 1l8 8-8 8" fill="none" stroke="#333" stroke-width="2"/></svg>
</section>

<footer class="site-footer abs">
  <div class="f-col" style="left:173px;width:200px">
    <h4>Contact Us</h4>
    <p>Brambleview Wellness Centre<br>88 Larkspur Avenue East, Suite 210<br>Toronto, Ontario, M4X 2C9</p>
    <p>Phone: 416-555-0182<br>Fax: 416-555-0147</p>
    <div class="pill pill-green f-btn"><span class="cal"></span>Book An Appointment</div>
  </div>
  <div class="f-col" style="left:392px;width:190px">
    <h4>Hours of Operation</h4>
    <p>We are open for business at 7:30 am. Open 7 days a week!</p>
    <p>Monday to Friday:<br>7:30am - 8pm</p>
    <p>Saturday to Sunday:<br>10am - 5pm</p>
  </div>
  <div class="f-col" style="left:610px;width:210px">
    <h4>Our Tweets</h4>
    <div class="tweet"><span class="av" role="img" aria-label="Profile photo"></span><div>Brambleview Wellness<br>@BrambleviewWell<br>http://fb.me/9kq2x7Lm<br>30 Aug 2017</div></div>
    <div class="tweet"><span class="av" role="img" aria-label="Profile photo"></span><div>Brambleview Wellness<br>@BrambleviewWell<br>http://fb.me/9kq2x7Lm<br>30 Aug 2017</div></div>
  </div>
  <div class="badge" role="img" aria-label="Award badge"></div>
  <p class="badge-note">Brambleview Wellness Centre is ranked as a top Wellness Centre in Toronto ON<br>Verified by Bookwren.com</p>
  <div class="f-rule"></div>
  <div class="social"><span></span><span></span></div>
  <p class="copyright">Copyright © 2017 Brambleview Wellness Centre</p>
</footer>

</body>
</html>
```